Visitenkarten-Design für Landschaftspfleger
Zielgruppe
Wir sind Landschaftspfleger kritischer Infrastruktur. Unsere Zielgruppe ist das operativer Management Großer Energiekonzerne die den Einkauf managen, Ausschreibungen und Vergabemaßnahmen organisieren.
Aufgabenstellung
Die Designs sollen nur die Logofarben enthalten, Weniger ist mehr.
Slogan:
Moderne Trassenpflege erhält LEBENSRÄUME!
Adresse: Lindenauer Weg 12
15832 Ostrauer Feld
Karl Wendtberg
MBA Agrarmanagement
Projektleiter Trassen- / Stationspflege
Telefon:01529347816
mail: karl.wendtberg@vorlux.de
www.vorlux.de

```html
<!DOCTYPE html>
<html lang="de">
<head>
<meta charset="utf-8">
<title>Visitenkarte – Karl Wendtberg</title>
<link rel="stylesheet" href="https://fonts.googleapis.com/css2?family=Inter:wght@300;400&family=Source+Serif+4:opsz,wght@8..60,500&display=swap">
<style>
  :root {
    --paper: #ebe7e1;
    --ink: #141414;
    --ink-soft: #3a3836;
    --wheat: #d8cec1;
    --wheat-soft: rgba(216, 206, 193, 0);
  }
  html, body {
    margin: 0;
    padding: 0;
    width: 1200px;
    height: 900px;
    overflow: hidden;
    background: var(--paper);
  }
  .card {
    position: relative;
    width: 1200px;
    height: 900px;
    background: var(--paper);
    color: var(--ink);
  }
  .wheat-motif {
    position: absolute;
    left: 380px;
    top: 80px;
    width: 580px;
    height: 820px;
    background: radial-gradient(ellipse 45% 50% at 60% 35%, var(--wheat) 0%, var(--wheat-soft) 75%);
    opacity: 0.6;
  }
  .identity {
    position: absolute;
    left: 123px;
    top: 478px;
    width: 473px;
  }
  .identity__name {
    margin: 0;
    font-family: "Source Serif 4", Georgia, serif;
    font-weight: 500;
    font-size: 82px;
    line-height: 80px;
    letter-spacing: -1px;
  }
  .identity__rule {
    height: 2px;
    background: var(--ink);
    margin-top: 16px;
    width: 473px;
  }
  .identity__role {
    margin: 18px 0 0;
    font-family: "Inter", Arial, sans-serif;
    font-weight: 400;
    font-size: 27px;
    line-height: 44px;
  }
  .slogan {
    position: absolute;
    left: 700px;
    top: 400px;
    margin: 0;
    font-family: "Inter", Arial, sans-serif;
    font-weight: 300;
    font-size: 46px;
    line-height: 52px;
    letter-spacing: -0.5px;
  }
  .contact {
    position: absolute;
    left: 700px;
    top: 650px;
    margin: 0;
    font-family: "Inter", Arial, sans-serif;
    font-style: normal;
    font-weight: 400;
    font-size: 20px;
    line-height: 32px;
    color: var(--ink-soft);
  }
</style>
</head>
<body>
  <main class="card">
    <div class="wheat-motif" role="img" aria-label="Zarte, blasse Weizenähre mit geschwungenem Halm als Hintergrundmotiv"></div>

    <section class="identity">
      <h1 class="identity__name">Karl<br>Wendtberg</h1>
      <div class="identity__rule"></div>
      <p class="identity__role">MBA Agrarmanagement -<br>Project Lead</p>
    </section>

    <p class="slogan">MODERNE<br>TRASSENPFLEGE<br>ERHÄLT<br>LEBENSRÄUME!</p>

    <address class="contact">
      Lindenauer Weg 12<br>
      15832 Ostrauer Feld<br>
      Telefon: 01529347816<br>
      karl.wendtberg@vorlux.de<br>
      www.vorlux.de
    </address>
  </main>
</body>
</html>
```